Searchable website that will contain information about sites for Bright Harbor Roster.

Once a search is performed the website will show the following information per site:
Title, Description, Screenshot of the site. I'm thinking three items per row.

Number of Pages Required

1 page

Font styles to use
Sans Serif

Colors
ffffff
3176b5

```html
<!DOCTYPE html>
<html lang="en">
<head>
<meta charset="utf-8">
<title>Harbor Vouched — Bright Harbor Roster</title>
<link rel="stylesheet" href="https://fonts.googleapis.com/css2?family=Poppins:wght@300;400;500;600;700&family=Open+Sans:wght@400;600;700&display=swap">
<style>
:root{
  --blue:#3176b5;
  --blue-deep:#2a62ad;
  --blue-band:#2c62ae;
  --nav-a:#2f6fc4;
  --nav-b:#4a8ee0;
  --white:#ffffff;
  --ink:#222222;
  --muted:#555555;
  --star:#b6c51b;
  --footer:#1e1e1e;
  --line:#dddddd;
}
*{box-sizing:border-box;margin:0;padding:0}
html,body{width:1200px;height:3358px;overflow:hidden;background:var(--white)}
body{position:relative;font-family:"Open Sans",Arial,sans-serif;color:var(--ink)}
.abs{position:absolute}

/* header */
.site-header{left:0;top:0;width:1200px;height:103px;background:#f4f4f4}
.brand{left:88px;top:28px;font-family:"Poppins",sans-serif;font-weight:400;font-size:38px;color:var(--blue-deep);letter-spacing:.5px}
.social{right:88px;top:41px;display:flex;gap:20px}
.social span{width:20px;height:20px;background:var(--blue-deep);border-radius:3px;display:block}

.main-nav{left:0;top:103px;width:1200px;height:60px;background:linear-gradient(90deg,var(--nav-a),var(--nav-b))}
.main-nav ul{list-style:none;display:flex;gap:34px;position:absolute;left:86px;top:18px;font-family:"Poppins",sans-serif;font-size:15px;color:var(--white)}
.main-nav li.active{font-weight:600}
.login{right:90px;top:11px;width:92px;height:38px;border-radius:19px;background:var(--white);color:var(--blue-deep);font-family:"Poppins",sans-serif;font-size:15px;text-align:center;line-height:38px}

/* hero */
.hero{left:0;top:163px;width:1200px;height:553px;background:radial-gradient(ellipse at 55% 40%,#4b4a48 0%,#2a2b2d 45%,#15181c 100%)}
.hero h1{position:absolute;left:0;width:1200px;top:222px;text-align:center;font-family:"Poppins",sans-serif;font-weight:700;font-size:46px;color:var(--white);letter-spacing:-1px}
.search{left:352px;top:314px;width:496px;height:54px;border-radius:27px;background:var(--white)}
.search .ph{position:absolute;left:40px;top:15px;font-size:18px;color:#555}
.search svg{position:absolute;left:18px;top:19px}
.search .go{position:absolute;right:0;top:0;width:132px;height:54px;border-radius:27px;background:var(--blue);border:2px solid var(--white);color:var(--white);font-family:"Poppins",sans-serif;font-size:18px;text-align:center;line-height:50px}
.dots{left:572px;top:518px;display:flex;gap:10px}
.dots span{width:11px;height:11px;border-radius:50%;border:2px solid var(--nav-b)}
.dots span.on{background:var(--nav-b)}

/* results */
.section-title{font-family:"Poppins",sans-serif;font-weight:600;color:var(--blue-deep)}
.results-title{left:93px;top:766px;font-size:30px}
.sort{left:893px;top:763px;width:217px;height:37px;border:1px solid #ccc;box-shadow:0 1px 3px rgba(0,0,0,.15);font-size:13px;color:#666;padding:9px 12px}
.sort svg{position:absolute;right:14px;top:15px}

.site-card{width:336px;height:363px;background:var(--white);box-shadow:0 1px 6px rgba(0,0,0,.25)}
.site-card .shot{width:336px;height:223px}
.site-card .row{display:flex;justify-content:space-between;align-items:center;padding:14px 18px 4px 16px}
.site-card h3{font-family:"Poppins",sans-serif;font-size:18px;font-weight:600;color:var(--blue-deep)}
.stars{display:flex;gap:2px}
.site-card p{padding:0 16px;font-size:15px;line-height:26px;color:var(--ink)}

.pager{left:486px;top:1652px;display:flex;gap:15px;align-items:center;font-family:"Poppins",sans-serif;font-size:15px}
.pager .pg{width:42px;height:42px;border-radius:50%;border:1px solid #ccc;text-align:center;line-height:40px}
.pager .pg.on{background:var(--blue);border-color:var(--blue);color:var(--white)}
.pager .ar{width:14px;text-align:center}

/* about */
.about-title{left:100px;top:1800px;font-size:25px}
.about-text{left:100px;top:1860px;width:470px;font-size:16px;line-height:30px;color:#333}
.btn-more{left:100px;top:2066px;width:133px;height:40px;border-radius:20px;background:linear-gradient(90deg,var(--nav-a),var(--nav-b));color:var(--white);font-family:"Poppins",sans-serif;font-weight:600;font-size:15px;text-align:center;line-height:40px}
.about-frame{left:876px;top:1793px;width:237px;height:327px;background:var(--nav-b)}
.about-photo{left:628px;top:1810px;width:468px;height:295px;background:linear-gradient(135deg,#c9cdd2,#6d7886 50%,#2d4f8c)}

/* testimonials */
.testimonials{left:0;top:2212px;width:1200px;height:508px;background:var(--blue-band);color:var(--white)}
.testimonials h2{position:absolute;left:0;width:1200px;top:50px;text-align:center;font-family:"Poppins",sans-serif;font-size:24px;font-weight:600}
.quote-open{left:288px;top:98px}
.quote-close{left:862px;top:204px}
.testimonials blockquote{position:absolute;left:290px;width:620px;top:164px;text-align:center;font-size:15px;line-height:27px}
.testimonials .who{position:absolute;left:0;width:1200px;top:218px;text-align:center;font-family:"Poppins",sans-serif;font-size:20px;letter-spacing:.5px}
.avatar{position:absolute;border-radius:50%;background:linear-gradient(160deg,#9fb2c8,#465b78);border:3px solid rgba(255,255,255,.4)}
.avatar.main{border:4px solid var(--white);background:linear-gradient(160deg,#c9ccd1,#5b4b40)}
.t-arrow{top:325px}
.t-track{left:197px;top:445px;width:806px;height:2px;background:rgba(255,255,255,.35)}
.t-thumb{left:555px;top:443px;width:90px;height:5px;background:var(--white)}

/* articles */
.articles-title{left:0;width:1200px;top:2762px;text-align:center;font-size:25px}
.post{width:325px;height:365px;background:var(--white);box-shadow:0 1px 6px rgba(0,0,0,.15)}
.post .img{position:absolute;left:62px;top:0;width:253px;height:165px;background:linear-gradient(180deg,#3b4a66 0%,#c26b3b 48%,#2a2f3b 70%,#17202c 100%)}
.post .date{position:absolute;left:0;top:0;width:50px;height:72px;background:var(--white);border:1px solid #e4e4e4;text-align:center;font-family:"Poppins",sans-serif}
.post .date b{display:block;font-size:17px;margin-top:10px}
.post .date i{font-style:normal;font-size:13px;font-weight:600}
.post .cmt{position:absolute;left:0;top:72px;width:50px;height:34px;background:var(--blue);color:var(--white);font-size:11px;display:flex;align-items:center;justify-content:center;gap:5px}
.post .body{position:absolute;left:62px;top:184px;width:240px;font-size:12px;line-height:22px}
.post .meta{color:var(--blue);font-size:11px}
.post .head{font-weight:700;font-size:12px;margin-top:4px}
.post .ex{color:#555;margin-top:2px}
.post .more{color:var(--blue);text-decoration:underline;font-size:11px;margin-top:8px}

/* footer */
.site-footer{left:0;top:3248px;width:1200px;height:110px;background:var(--footer);color:var(--white)}
.f-icons{position:absolute;left:538px;top:32px;display:flex;gap:8px}
.f-icons span{width:11px;height:11px;background:var(--white);border-radius:2px}
.copyright{position:absolute;left:0;width:1200px;top:70px;text-align:center;font-size:13px}
</style>
</head>
<body>

<header class="abs site-header">
  <div class="abs brand">HARBOR VOUCHED</div>
  <div class="abs social" aria-label="Social links"><span></span><span></span><span></span><span></span><span></span></div>
</header>

<nav class="abs main-nav">
  <ul><li class="active">Home</li><li>About us</li><li>Services</li><li>Entrepreneur</li><li>Blog</li><li>Contact Us</li></ul>
  <div class="abs login">Login</div>
</nav>

<section class="abs hero" role="img" aria-label="Man working on a laptop at a desk in a dim office">
  <h1>ONLINE ENTREPRENEURS</h1>
  <div class="abs search">
    <svg width="14" height="14" viewBox="0 0 14 14"><circle cx="6" cy="6" r="4.5" fill="none" stroke="#444" stroke-width="2"/><line x1="9.3" y1="9.3" x2="13" y2="13" stroke="#444" stroke-width="2"/></svg>
    <span class="ph">Search for Online Entrepreneurs</span>
    <span class="go">Search</span>
  </div>
  <div class="abs dots"><span></span><span class="on"></span><span></span></div>
</section>

<h2 class="abs section-title results-title">Search results</h2>
<div class="abs sort">Sort by
  <svg width="8" height="6" viewBox="0 0 8 6"><path d="M0 0h8L4 6z" fill="#2a62ad"/></svg>
</div>

<!-- result cards -->
<article class="abs site-card" style="left:86px;top:860px">
  <div class="shot" role="img" aria-label="Site screenshot: massage therapy booking page" style="background:linear-gradient(120deg,#5a5a5a,#2b2b2b 60%,#d9d9d9)"></div>
  <div class="row"><h3>SITE NAME</h3><div class="stars"><svg width="94" height="17" viewBox="0 0 94 17"><g fill="#b6c51b"><path id="st" d="M8.5 0l2.6 5.3 5.9.8-4.3 4.1 1 5.8-5.2-2.7-5.2 2.7 1-5.8L0 6.1l5.9-.8z"/><use href="#st" x="19"/><use href="#st" x="38"/><use href="#st" x="57"/><use href="#st" x="76"/></g></svg></div></div>
  <p>Sed ut perspiciatis unde omnis iste natus error sit voluptatem accusantium dolore laudantium</p>
</article>
<article class="abs site-card" style="left:434px;top:860px">
  <div class="shot" role="img" aria-label="Site screenshot: woodworking craftsmanship page" style="background:linear-gradient(120deg,#2a2420,#6b4a33 60%,#2d2520)"></div>
  <div class="row"><h3>SITE NAME</h3><svg width="94" height="17" viewBox="0 0 94 17"><g fill="#b6c51b"><use href="#st"/><use href="#st" x="19"/><use href="#st" x="38"/><use href="#st" x="57"/><use href="#st" x="76"/></g></svg></div>
  <p>Sed ut perspiciatis unde omnis iste natus error sit voluptatem accusantium dolore laudantium</p>
</article>
<article class="abs site-card" style="left:776px;top:860px">
  <div class="shot" role="img" aria-label="Site screenshot: hair salon booking page" style="background:linear-gradient(120deg,#3a3a3a,#8a8580 55%,#c8c2bb)"></div>
  <div class="row"><h3>SITE NAME</h3><svg width="94" height="17" viewBox="0 0 94 17"><g fill="#b6c51b"><use href="#st"/><use href="#st" x="19"/><use href="#st" x="38"/><use href="#st" x="57"/><use href="#st" x="76"/></g></svg></div>
  <p>Sed ut perspiciatis unde omnis iste natus error sit voluptatem accusantium dolore laudantium</p>
</article>
<article class="abs site-card" style="left:86px;top:1233px">
  <div class="shot" role="img" aria-label="Site screenshot: accounting services page" style="background:linear-gradient(120deg,#d6d6d6,#8d8d8d 50%,#3e3e3e)"></div>
  <div class="row"><h3>SITE NAME</h3><svg width="94" height="17" viewBox="0 0 94 17"><g fill="#b6c51b"><use href="#st"/><use href="#st" x="19"/><use href="#st" x="38"/><use href="#st" x="57"/><use href="#st" x="76"/></g></svg></div>
  <p>Sed ut perspiciatis unde omnis iste natus error sit voluptatem accusantium dolore laudantium</p>
</article>
<article class="abs site-card" style="left:434px;top:1233px">
  <div class="shot" role="img" aria-label="Site screenshot: barber shop booking page" style="background:linear-gradient(120deg,#2c2c2c,#555250 55%,#1d1d1d)"></div>
  <div class="row"><h3>SITE NAME</h3><svg width="94" height="17" viewBox="0 0 94 17"><g fill="#b6c51b"><use href="#st"/><use href="#st" x="19"/><use href="#st" x="38"/><use href="#st" x="57"/><use href="#st" x="76"/></g></svg></div>
  <p>Sed ut perspiciatis unde omnis iste natus error sit voluptatem accusantium dolore laudantium</p>
</article>
<article class="abs site-card" style="left:776px;top:1233px">
  <div class="shot" role="img" aria-label="Site screenshot: business advice contact page" style="background:linear-gradient(120deg,#bfb6ab,#d9d2ca 50%,#7c6a5a)"></div>
  <div class="row"><h3>SITE NAME</h3><svg width="94" height="17" viewBox="0 0 94 17"><g fill="#b6c51b"><use href="#st"/><use href="#st" x="19"/><use href="#st" x="38"/><use href="#st" x="57"/><use href="#st" x="76"/></g></svg></div>
  <p>Sed ut perspiciatis unde omnis iste natus error sit voluptatem accusantium dolore laudantium</p>
</article>

<div class="abs pager"><span class="ar">«</span><span class="pg on">1</span><span class="pg">2</span><span class="pg">3</span><span class="ar">»</span></div>

<!-- about -->
<h2 class="abs section-title about-title">ABOUT US</h2>
<p class="abs about-text">Lorem ipsum dolor sit amet, consectetur adipiscing elit, sed do eiusmod tempor incididunt ut labore et dolore magna aliqua. Ut enim ad minim veniam, quis nostrud exercitation ullamco laboris nisi ut aliquip ex ea commodo consequat. Duis aute irure dolor in reprehenderit in voluptate velit esse cillum dolore eu fugiat nulla pariatur.</p>
<div class="abs btn-more">Read More</div>
<div class="abs about-frame"></div>
<div class="abs about-photo" role="img" aria-label="Man on the phone at an office desk taking notes"></div>

<!-- testimonials -->
<section class="abs testimonials">
  <h2>TESTIMONIALS</h2>
  <svg class="abs quote-open" width="60" height="46" viewBox="0 0 60 46"><g fill="#fff"><circle cx="13" cy="32" r="12"/><path d="M3 30C3 14 12 4 24 1l2 5C16 10 12 18 13 28z"/><circle cx="45" cy="32" r="12"/><path d="M35 30C35 14 44 4 56 1l2 5C48 10 44 18 45 28z"/></g></svg>
  <blockquote>At vero eos et accusamus et iusto odio dignissimos ducimus qui blanditiis praesentium voluptatum</blockquote>
  <div class="who">MILES ARDEN</div>
  <svg class="abs quote-close" width="60" height="46" viewBox="0 0 60 46"><g fill="#fff" transform="rotate(180 30 23)"><circle cx="13" cy="32" r="12"/><path d="M3 30C3 14 12 4 24 1l2 5C16 10 12 18 13 28z"/><circle cx="45" cy="32" r="12"/><path d="M35 30C35 14 44 4 56 1l2 5C48 10 44 18 45 28z"/></g></svg>

  <svg class="abs t-arrow" style="left:184px" width="22" height="38" viewBox="0 0 22 38"><path d="M19 3L4 19l15 16" fill="none" stroke="#fff" stroke-width="4"/></svg>
  <div class="avatar" role="img" aria-label="Client portrait" style="left:275px;top:305px;width:84px;height:84px"></div>
  <div class="avatar" role="img" aria-label="Client portrait" style="left:403px;top:305px;width:84px;height:84px"></div>
  <div class="avatar main" role="img" aria-label="Featured client portrait" style="left:547px;top:293px;width:106px;height:106px"></div>
  <div class="avatar" role="img" aria-label="Client portrait" style="left:713px;top:305px;width:84px;height:84px"></div>
  <div class="avatar" role="img" aria-label="Client portrait" style="left:841px;top:305px;width:84px;height:84px"></div>
  <svg class="abs t-arrow" style="left:986px" width="22" height="38" viewBox="0 0 22 38"><path d="M3 3l15 16L3 35" fill="none" stroke="#fff" stroke-width="4"/></svg>
  <div class="abs t-track"></div>
  <div class="abs t-thumb"></div>
</section>

<!-- articles -->
<h2 class="abs section-title articles-title">ARTICLES</h2>

<article class="abs post" style="left:105px;top:2860px">
  <div class="img" role="img" aria-label="Kayak on a lake at sunset"></div>
  <div class="date"><b>30</b><i>Aug</i></div>
  <div class="cmt"><svg width="12" height="10" viewBox="0 0 12 10"><path d="M1 1h10v6H5l-3 3V7H1z" fill="#fff"/></svg>25</div>
  <div class="body"><div class="meta">Consectetur &nbsp;| &nbsp;By Someone</div><div class="head">Nullam ac vestibulum orci, in mattis ipsum.</div><div class="ex">Lorem ipsum dolor sit amet, consectetur adipiscing elit. Morbi egestas arcu vel quam consequat.</div><div class="more">Read More...</div></div>
</article>
<article class="abs post" style="left:444px;top:2860px">
  <div class="img" role="img" aria-label="Kayak on a lake at sunset"></div>
  <div class="date"><b>2</b><i>Aug</i></div>
  <div class="cmt"><svg width="12" height="10" viewBox="0 0 12 10"><path d="M1 1h10v6H5l-3 3V7H1z" fill="#fff"/></svg>25</div>
  <div class="body"><div class="meta">Consectetur &nbsp;| &nbsp;By Someone</div><div class="head">Nullam ac vestibulum orci, in mattis ipsum.</div><div class="ex">Lorem ipsum dolor sit amet, consectetur adipiscing elit. Morbi egestas arcu vel quam consequat.</div><div class="more">Read More...</div></div>
</article>
<article class="abs post" style="left:780px;top:2860px">
  <div class="img" role="img" aria-label="Kayak on a lake at sunset"></div>
  <div class="date"><b>2</b><i>Aug</i></div>
  <div class="cmt"><svg width="12" height="10" viewBox="0 0 12 10"><path d="M1 1h10v6H5l-3 3V7H1z" fill="#fff"/></svg>25</div>
  <div class="body"><div class="meta">Consectetur &nbsp;| &nbsp;By Someone</div><div class="head">Nullam ac vestibulum orci, in mattis ipsum.</div><div class="ex">Lorem ipsum dolor sit amet, consectetur adipiscing elit. Morbi egestas arcu vel quam consequat.</div><div class="more">Read More...</div></div>
</article>

<footer class="abs site-footer">
  <div class="f-icons" aria-label="Social links"><span></span><span></span><span></span><span></span><span></span><span></span></div>
  <div class="copyright">Copyright © 2018. All Rights Reserved.</div>
</footer>

</body>
</html>
```